Pet Sitting Business Card

Would like a business card designed for my new pet sitting business
Card needs to match with logo design.
Blue and Orange are the theme colours.

Simple yet sophisticated design

company name:- MARIGOLD PET CARE
Dana Corbel
Owner
0472615390
dana@marigoldpetcare.com.au
www.marigoldpetcare.com.au

I'm going to close my deadline early. I will be picking a winner by the 10th of May. Please submit designs before then.
thank you

Target Market(s)

All types of professional pet lovers wishing to have their pet looked after

Industry/Entity Type

Pet

Requirements
Must have
• Logo design
Blue and orange

```html
<!DOCTYPE html>
<html lang="en">
<head>
<meta charset="utf-8">
<title>Marigold Pet Care – Business Card</title>
<link href="https://fonts.googleapis.com/css2?family=Tinos:ital,wght@0,400;0,700;1,400;1,700&display=swap" rel="stylesheet">
<style>
  :root {
    --backdrop: #e4e5e7;
    --card: #ffffff;
    --brand-blue: #2a93e6;
    --brand-orange: #e8852b;
    --card-shadow: rgba(0, 0, 0, 0.18);
  }
  html, body {
    margin: 0;
    padding: 0;
    overflow: hidden;
  }
  .canvas {
    position: relative;
    width: 1200px;
    height: 849px;
    background: var(--backdrop);
    overflow: hidden;
    font-family: "Tinos", "Times New Roman", serif;
  }
  .card {
    position: absolute;
    top: 238px;
    width: 500px;
    height: 372px;
    background: var(--card);
    border-radius: 58px;
    box-shadow: 0 10px 30px var(--card-shadow);
    display: flex;
    flex-direction: column;
    align-items: center;
  }
  .card--front { left: 70px; justify-content: center; }
  .card--back { left: 630px; padding-top: 44px; box-sizing: border-box; }

  .brand {
    display: flex;
    flex-direction: column;
    align-items: center;
  }
  .brand__dot {
    border-radius: 50%;
    background: var(--brand-orange);
  }
  .brand__name {
    margin: 0;
    font-weight: 700;
    color: var(--brand-blue);
    letter-spacing: 0.04em;
    text-align: center;
    line-height: 1.05;
  }
  .card--front .brand__dot { width: 44px; height: 44px; margin-bottom: 18px; }
  .card--front .brand__name { font-size: 44px; }
  .card--back .brand__dot { width: 26px; height: 26px; margin-bottom: 10px; }
  .card--back .brand__name { font-size: 24px; }

  .person {
    margin-top: 38px;
    text-align: center;
  }
  .person__name {
    margin: 0;
    font-size: 27px;
    font-weight: 700;
    font-style: italic;
    color: var(--brand-blue);
  }
  .person__role {
    margin: 4px 0 0;
    font-size: 20px;
    font-style: italic;
    color: var(--brand-orange);
  }
  .contact {
    margin-top: 34px;
    list-style: none;
    padding: 0;
    text-align: center;
    color: var(--brand-orange);
    font-size: 19px;
    line-height: 1.36;
  }
  .contact__phone {
    display: inline-flex;
    align-items: center;
    gap: 7px;
  }
  .contact__icon { width: 16px; height: 16px; fill: var(--brand-orange); }
</style>
</head>
<body>
<main class="canvas">
  <section class="card card--front" aria-label="Card front">
    <div class="brand">
      <span class="brand__dot" aria-hidden="true"></span>
      <h1 class="brand__name">MARIGOLD PET CARE</h1>
    </div>
  </section>

  <section class="card card--back" aria-label="Card back">
    <div class="brand">
      <span class="brand__dot" aria-hidden="true"></span>
      <p class="brand__name">MARIGOLD PET CARE</p>
    </div>
    <div class="person">
      <h2 class="person__name">Dana Corbel</h2>
      <p class="person__role">Owner</p>
    </div>
    <ul class="contact">
      <li class="contact__phone">
        <svg class="contact__icon" viewBox="0 0 24 24" aria-hidden="true">
          <path d="M3 8c0-2 2-4 9-4s9 2 9 4v2h-5V8H8v2H3z"/>
          <path d="M6 11h12l2 9H4z M12 13a3 3 0 1 0 0 6a3 3 0 1 0 0-6z"/>
        </svg>
        0472615390
      </li>
      <li>dana@marigoldpetcare.com.au</li>
      <li>www.marigoldpetcare.com.au</li>
    </ul>
  </section>
</main>
</body>
</html>
```